KVR Associates needs a web site

We need a web site for www.kvrassociates-example.com. KVR is a mergers and acquisition consulting company that focuses our buyer and seller services on logistics companies. We help put companies together, and help with legal and financial due diligence. We want the web site to express our service and show the logistics components. We want personalized images versus pictures of trucks and airplanes.

Our new logo uses Burgandy and grey colors. Image attached. We are not in to bold, big letters...classy, artistic, low key preferred. Confidentiality, experience, professional are what we want to express on the site.

All we expect for the first part of this project is a home page, and one subpage.  We are budgeting other funds for the technical aspects of the web site

Reason: All that I'm seeing so far is trucks, forklifts and planes. We are a legal mergers and acquisitions firm that focus on logistics. I like some of the images to say logistics, but really want it say legal, financial, and putting companies together. Will pay extra for the sub page if someone can impress us with a home page.

Reason: Swamped with another project at the moment...will work on this over the weekend and provide designer feedback and select final design by Tuesday

```html
<!DOCTYPE html>
<html lang="en">
<head>
<meta charset="utf-8">
<title>KVR Associates</title>
<link rel="stylesheet" href="https://fonts.googleapis.com/css2?family=Arimo:ital,wght@0,400;0,700;1,400;1,700&family=Roboto+Condensed:wght@300;400&display=swap">
<style>
  :root {
    --burgundy: #a60f38;
    --burgundy-deep: #9e0c33;
    --charcoal: #333333;
    --ink: #1b1b1b;
    --footer: #222222;
    --text-dark: #2b2b2b;
    --text-body: #4a4a4a;
    --white: #ffffff;
    --grey-light: #d4d2d2;
    --social: #3b6fb0;
  }
  * { margin: 0; padding: 0; box-sizing: border-box; }
  html, body { width: 746px; height: 1200px; overflow: hidden; background: var(--white); }
  body { font-family: "Arimo", Arial, sans-serif; color: var(--text-dark); }
  .page { position: relative; width: 746px; height: 1200px; overflow: hidden; }
  .abs { position: absolute; }

  /* header */
  .top-rule { left: 0; top: 0; width: 746px; height: 5px; background: #5a5a5a; }
  .brand { left: 0; top: 5px; width: 746px; height: 74px; display: flex; align-items: center; justify-content: center; gap: 10px; }
  .brand-mark { width: 14px; height: 14px; background: var(--burgundy); }
  .brand-name { font-family: "Roboto Condensed", sans-serif; font-weight: 400; font-size: 26px; letter-spacing: 1px; color: #555555; }

  /* navigation */
  .main-nav { left: 0; top: 79px; width: 746px; height: 30px; background: var(--charcoal); }
  .nav-item { position: absolute; top: 0; height: 30px; line-height: 30px; font-size: 7px; color: var(--white); text-align: center; white-space: nowrap; text-transform: uppercase; }
  .nav-item.is-active { background: var(--burgundy); }

  /* hero */
  .hero { left: 0; top: 109px; width: 746px; height: 282px;
    background:
      linear-gradient(180deg, rgba(0,0,0,0) 60%, rgba(40,40,45,0.85) 100%),
      radial-gradient(circle at 18% 42%, #e9b66a 0%, rgba(233,182,106,0) 18%),
      linear-gradient(90deg, #3d4a2c 0%, #56613f 22%, #8c9aa6 45%, #cfd5da 60%, #8b98a3 80%, #5d6a74 100%); }
  .hero-title { left: 112px; top: 256px; font-size: 25px; line-height: 29px; color: var(--white); font-weight: 400; }
  .hero-caption { left: 110px; top: 320px; width: 270px; height: 36px; background: var(--burgundy); color: var(--white); font-size: 9.5px; line-height: 13.5px; padding: 4px 5px; }
  .hero-arrows { left: 380px; top: 314px; width: 32px; height: 44px; background: #1e1e1e; color: var(--white); font-size: 13px; line-height: 22px; text-align: center; }

  /* welcome */
  .welcome { left: 0; top: 391px; width: 746px; height: 115px; background: var(--ink); }
  .section-title { font-family: "Roboto Condensed", sans-serif; font-weight: 300; text-transform: uppercase; }
  .welcome-title { left: 110px; top: 404px; font-size: 23px; color: var(--burgundy); }
  .welcome-text { left: 110px; top: 436px; width: 524px; font-size: 7.7px; line-height: 12.8px; color: var(--white); text-align: justify; }

  /* services */
  .services-title { left: 110px; top: 524px; font-size: 20px; color: var(--text-dark); }
  .service-card { top: 562px; width: 168px; height: 193px; background: var(--ink); }
  .service-image { width: 168px; height: 88px; }
  .service-heading { height: 27px; background: var(--burgundy); color: var(--white); font-size: 12px; line-height: 27px; text-align: center; text-transform: uppercase; }
  .service-text { padding: 6px 9px 0; font-size: 6.6px; line-height: 10.8px; color: var(--white); text-align: justify; }
  .read-more { position: absolute; left: 57px; top: 177px; width: 53px; height: 16px; background: var(--burgundy); color: var(--white); font-size: 7px; line-height: 16px; text-align: center; letter-spacing: 0.3px; }
  .services-text { left: 110px; top: 776px; width: 528px; font-size: 7.5px; line-height: 13.6px; color: var(--text-body); text-align: justify; }

  /* testimonial */
  .testimonial { left: 0; top: 904px; width: 746px; height: 186px; background: var(--burgundy-deep); }
  .testimonial-title { left: 0; top: 911px; width: 746px; text-align: center; font-size: 25px; color: var(--white); }
  .avatar { left: 341px; top: 951px; width: 62px; height: 62px; border-radius: 50%; border: 4px solid var(--white); background: radial-gradient(circle at 50% 40%, #d9c3ae 0%, #a89b90 70%, #8f8a86 100%); }
  .quote-mark { font-family: "Arimo", sans-serif; font-weight: 700; font-style: italic; font-size: 17px; color: var(--white); }
  .quote-text { left: 118px; top: 1024px; width: 516px; font-size: 8.4px; line-height: 12px; font-style: italic; color: var(--white); text-align: center; }
  .quote-author { left: 0; top: 1059px; width: 746px; text-align: center; font-size: 10px; font-weight: 700; font-style: italic; color: var(--white); }

  /* footer */
  .footer { left: 0; top: 1090px; width: 746px; height: 110px; background: var(--footer); }
  .footer-nav .nav-item { top: 1090px; height: 28px; line-height: 28px; }
  .footer-nav .nav-item.is-active { background: var(--grey-light); color: var(--text-dark); }
  .social { top: 1145px; width: 16px; height: 16px; border-radius: 2px; background: var(--social); }
  .copyright { left: 0; top: 1174px; width: 746px; text-align: center; font-size: 6.5px; color: var(--white); text-transform: uppercase; }
</style>
</head>
<body>
<div class="page">
  <div class="abs top-rule"></div>

  <header class="abs brand">
    <span class="brand-mark"></span>
    <span class="brand-name">KVR Associates</span>
  </header>

  <nav class="abs main-nav">
    <a class="nav-item is-active" style="left:150px;width:44px">Home</a>
    <a class="nav-item" style="left:194px;width:60px">About Us</a>
    <a class="nav-item" style="left:254px;width:40px">Services</a>
    <a class="nav-item" style="left:294px;width:96px">Request a Quote</a>
    <a class="nav-item" style="left:390px;width:64px">Office Networks</a>
    <a class="nav-item" style="left:454px;width:84px">Contact Us</a>
    <a class="nav-item" style="left:538px;width:40px">General Info</a>
  </nav>

  <section class="abs hero" role="img" aria-label="Photo of a refrigerated truck on a highway at sunset"></section>
  <h1 class="abs hero-title" style="font-weight:400">Lorem ipsum dolor<br>sit amet consectetur</h1>
  <p class="abs hero-caption">Lorem ipsum dolor sit amet, consectetur adipisicing elit, sed do eiusmod tempor incididunt ut labore et dolore magna aliqua.</p>
  <div class="abs hero-arrows">&lt;<br>&gt;</div>

  <section class="abs welcome"></section>
  <h2 class="abs section-title welcome-title">Welcome to KVR</h2>
  <p class="abs welcome-text">Lorem ipsum dolor sit amet, consectetur adipisicing elit, sed do eiusmod tempor incididunt ut labore et dolore magna aliqua. Ut enim ad minim veniam, quis nostrud exercitation ullamco laboris nisi ut aliquip ex ea commodo consequat. Duis aute irure dolor in reprehenderit in voluptate velit esse cillum dolore eu fugiat nulla pariatur. Excepteur sint occaecat cupidatat non proident, sunt in culpa qui officia deserunt mollit anim id est laborum</p>

  <h2 class="abs section-title services-title">Services</h2>

  <article class="abs service-card" style="left:110px">
    <div class="service-image" role="img" aria-label="Photo of a container ship at sea" style="background:linear-gradient(160deg,#c9d3dc 0%,#8a2a35 45%,#5a6f80 75%,#3f5566 100%)"></div>
    <h3 class="service-heading" style="font-weight:400">Lorem ipsum dolor</h3>
    <p class="service-text">Lorem ipsum dolor sit amet, consectetur adipisicing elit, sed do eiusmod tempor incididunt ut labore et dolore magna aliqua. Ut enim ad minim veniam, quis nostrud exercitation ullamco laboris</p>
    <a class="read-more">Read More</a>
  </article>

  <article class="abs service-card" style="left:290px">
    <div class="service-image" role="img" aria-label="Photo of a blue freight truck" style="background:linear-gradient(160deg,#dfe5ea 0%,#b9c3cb 40%,#2f6fa8 70%,#4d5a66 100%)"></div>
    <h3 class="service-heading" style="font-weight:400">Lorem ipsum dolor</h3>
    <p class="service-text">Lorem ipsum dolor sit amet, consectetur adipisicing elit, sed do eiusmod tempor incididunt ut labore et dolore magna aliqua. Ut enim ad minim veniam, quis nostrud exercitation ullamco laboris</p>
    <a class="read-more">Read More</a>
  </article>

  <article class="abs service-card" style="left:470px">
    <div class="service-image" role="img" aria-label="Photo of a passenger jet in a blue sky" style="background:linear-gradient(180deg,#2f5f93 0%,#6f97bf 55%,#c9d8e6 100%)"></div>
    <h3 class="service-heading" style="font-weight:400">Lorem ipsum dolor</h3>
    <p class="service-text">Lorem ipsum dolor sit amet, consectetur adipisicing elit, sed do eiusmod tempor incididunt ut labore et dolore magna aliqua. Ut enim ad minim veniam, quis nostrud exercitation ullamco laboris</p>
    <a class="read-more">Read More</a>
  </article>

  <p class="abs services-text">Lorem ipsum dolor sit amet, consectetur adipisicing elit, sed do eiusmod tempor incididunt ut labore et dolore magna aliqua. Ut enim ad minim veniam, quis nostrud exercitation ullamco laboris nisi ut aliquip ex ea commodo consequat. Duis aute irure dolor in reprehenderit in voluptate velit esse cillum dolore eu fugiat nulla pariatur. Excepteur sint occaecat cupidatat non proident, sunt in culpa qui officia deserunt mollit anim id est laborum Lorem ipsum dolor sit amet, consectetur adipisicing elit, sed do eiusmod tempor incididunt ut labore et dolore magna aliqua. Ut enim ad minim veniam, quis nostrud exercitation ullamco laboris nisi ut aliquip ex ea commodo consequat. Duis aute irure dolor in reprehenderit in voluptate velit esse cillum dolore eu fugiat nulla pariatur. Excepteur sint occaecat cupidatat non proident, sunt in culpa qui officia deserunt mollit anim id est laborum Lorem ipsum dolor sit amet, consectetur adipisicing elit, sed do eiusmod tempor incididunt ut labore et dolore magna aliqua.</p>

  <section class="abs testimonial"></section>
  <h2 class="abs section-title testimonial-title">Testimonial</h2>
  <div class="abs avatar" role="img" aria-label="Portrait photo of the client giving the testimonial"></div>
  <span class="abs quote-mark" style="left:112px;top:1010px">&rdquo;</span>
  <p class="abs quote-text">Lorem ipsum dolor sit amet, consectetur adipisicing elit, sed do eiusmod tempor incididunt ut labore et dolore magna aliqua. Ut enim ad minim veniam, quis nostrud exercitation ullamco laboris nisi ut aliquip ex ea commodo.</p>
  <span class="abs quote-mark" style="left:546px;top:1033px">&rdquo;</span>
  <p class="abs quote-author">Daniel Mercer</p>

  <footer class="abs footer"></footer>
  <nav class="footer-nav">
    <a class="abs nav-item is-active" style="left:121px;width:45px">Home</a>
    <a class="abs nav-item" style="left:169px;width:50px">About Us</a>
    <a class="abs nav-item" style="left:232px;width:50px">Services</a>
    <a class="abs nav-item" style="left:299px;width:80px">Request a Quote</a>
    <a class="abs nav-item" style="left:391px;width:80px">Office Networks</a>
    <a class="abs nav-item" style="left:479px;width:70px">Contact Us</a>
    <a class="abs nav-item" style="left:556px;width:70px">General Info</a>
  </nav>
  <a class="abs social" style="left:342px" aria-label="Social profile one"></a>
  <a class="abs social" style="left:365px" aria-label="Social profile two"></a>
  <a class="abs social" style="left:388px" aria-label="Social profile three"></a>
  <p class="abs copyright">Copyright &copy; 2013 / All Rights Reserved,</p>
</div>
</body>
</html>
```